Realtor branding business card

modern, simple and self branding. Broker office logo needs to be used but not emphasized. Looking to brand myself

Target Market(s)

buyers, sellers and investors

Industry/Entity Type

Realtor

Contact Information for Business Card

Sample of my current business card on file

Requirements
Must have
• my website - emilioverdaskt.com
• Realtor logo
• Fair housing logo
Nice to have
• Colors from office logo but not a must
Should not have
• Do not want headshot

```html
<!DOCTYPE html>
<html lang="en">
<head>
<meta charset="utf-8">
<title>Emilio Verdas, PA – Business Card</title>
<link href="https://fonts.googleapis.com/css2?family=Lato:wght@400;700;900&display=swap" rel="stylesheet">
<style>
  :root {
    --navy: #221466;
    --red: #d42020;
    --ink: #222222;
    --paper: #ffffff;
    --stage: #f1f1f1;
    --badge-line: #c9c5dc;
  }
  * { box-sizing: border-box; margin: 0; padding: 0; }
  html, body {
    width: 1200px; height: 757px; overflow: hidden;
    background: var(--stage);
    font-family: "Lato", sans-serif;
  }
  .canvas { position: relative; width: 1200px; height: 757px; }
  .card {
    position: absolute; top: 195px;
    width: 498px; height: 299px; overflow: hidden;
  }
  .card--front { left: 85px; background: var(--paper); }
  .card--back { left: 650px; background: var(--navy); }

  .brand {
    position: absolute; display: flex; align-items: center; gap: 7px;
    font-weight: 900; line-height: 1;
  }
  .brand__mark { width: 11px; height: 11px; flex: none; }
  .brand__name { display: flex; flex-direction: column; }
  .brand__line1 { font-size: 24px; letter-spacing: -0.3px; }
  .brand__line2 { font-size: 12.5px; letter-spacing: 0.5px; margin-top: 2px; }

  .card--front .brand { left: 34px; top: 56px; color: var(--navy); }
  .card--front .brand__mark { background: var(--red); }
  .card--back .brand { left: 31px; top: 222px; color: var(--paper); }
  .card--back .brand__mark { background: var(--paper); }

  .badges {
    position: absolute; right: 29px; top: 56px;
    display: flex; gap: 10px;
  }
  .badge {
    width: 36px; height: 36px;
    border: 2px solid var(--badge-line);
    background: var(--paper);
  }
  .badge--round { border-radius: 50%; }

  .contact { position: absolute; left: 34px; top: 195px; font-size: 10px; color: var(--ink); }
  .contact__row { display: flex; align-items: center; gap: 8px; height: 17px; }
  .contact__row svg { width: 11px; height: 10px; flex: none; }
  .contact__address { color: var(--navy); font-weight: 700; line-height: 15px; margin-top: 1px; }

  .agent { position: absolute; right: 29px; top: 204px; text-align: right; }
  .agent__name { color: var(--red); font-weight: 900; font-size: 20px; line-height: 1.1; }
  .agent__title { color: var(--ink); font-size: 11px; margin-top: 4px; }

  .rule { position: absolute; top: 273px; height: 4px; background: var(--navy); }
  .rule--left { left: 0; width: 360px; }
  .rule--right { left: 478px; right: 0; }
  .rule__star { position: absolute; left: 33px; top: 265px; width: 19px; height: 19px; }
  .website {
    position: absolute; left: 365px; top: 268px; width: 110px;
    font-size: 9.5px; font-weight: 700; color: var(--navy); white-space: nowrap;
  }
</style>
</head>
<body>
<main class="canvas">
  <section class="card card--front" aria-label="Business card front">
    <div class="brand">
      <span class="brand__mark"></span>
      <span class="brand__name">
        <span class="brand__line1">Brightpath</span>
        <span class="brand__line2">Realty Group</span>
      </span>
    </div>

    <div class="badges">
      <span class="badge" role="img" aria-label="Realtor membership badge"></span>
      <span class="badge badge--round" role="img" aria-label="Equal housing opportunity badge"></span>
    </div>

    <div class="contact">
      <div class="contact__row">
        <svg viewBox="0 0 11 10" aria-hidden="true"><path fill="#d42020" d="M1 3.5C1 1.5 3 1 5.5 1S10 1.5 10 3.5L8 4V3H3v1L1 3.5ZM2.5 5h6l1 4h-8l1-4Z"/></svg>
        <span>555.201.4830</span>
      </div>
      <div class="contact__row">
        <svg viewBox="0 0 11 10" aria-hidden="true"><rect x="0.5" y="1.5" width="10" height="7" fill="#d42020"/><path d="M0.5 1.5l5 4 5-4" fill="none" stroke="#fff" stroke-width="1"/></svg>
        <span>hello@brightpathfl.com</span>
      </div>
      <div class="contact__address">48 Lakeview Crest<br>Dr. Maple Springs, FL 30000</div>
    </div>

    <div class="agent">
      <div class="agent__name">Emilio Verdas, PA</div>
      <div class="agent__title">Realtor</div>
    </div>

    <div class="rule rule--left"></div>
    <svg class="rule__star" viewBox="0 0 20 20" aria-hidden="true"><polygon fill="#d42020" points="10,1 12.4,7.3 19,7.3 13.7,11.3 15.7,18 10,14 4.3,18 6.3,11.3 1,7.3 7.6,7.3"/></svg>
    <div class="website">www.emilioverdaskt.com</div>
    <div class="rule rule--right"></div>
  </section>

  <section class="card card--back" aria-label="Business card back">
    <div class="brand">
      <span class="brand__mark"></span>
      <span class="brand__name">
        <span class="brand__line1">Brightpath</span>
        <span class="brand__line2">Realty Group</span>
      </span>
    </div>
  </section>
</main>
</body>
</html>
```